Luma Harbor Vow Studio, Inc.

Luma Harbor Vow Studio Business Card design for Cardlyne. Clean, contemporary, creative, colorful (using colors provided). ONE SIDE SHOULD INCLUDE logo, www.lumaharborvowstudio.com, @sayidoatluma. OTHER SIDE SHOULD INCLUDE Delia Brennan. Owner & Officiant. Isabela, Puerto Rico. 555.014.2871. delia@lumaharborvowstudio.com. Colors are blue #58AA9E
and golden #e2bf80)

Target Market(s)

Destination Wedding Clients in the United States

Contact Information for Business Card

Delia Brennan
Owner & Officiant
Isabela, Puerto Rico
555.014.2871
delia@lumaharborvowstudio.com

Font styles to use
Sans Serif

Requirements
Must have
• Colorful (colors are blue #58AA9E
• and golden #e2bf80), clean, contemporary. ONE SIDE SHOULD INCLUDE logo, www.lumaharborvowstudio.com, @sayidoatluma. Other side should include Delia Brennan. Owner & Officiant. Isabela, Puerto Rico. 555.014.2871. delia@lumaharborvowstudio.com
Nice to have
• I would like to see a version that includes my bio photo, and one that doesn't include the bio photo

```html
<!DOCTYPE html>
<html lang="en">
<head>
<meta charset="utf-8">
<title>Luma Harbor Vow Studio – Business Card</title>
<link href="https://fonts.googleapis.com/css2?family=Lato:wght@300;400;700;900&display=swap" rel="stylesheet">
<style>
  :root {
    --teal: #58AA9E;
    --gold: #e2bf80;
    --white: #ffffff;
    --stage: #e6e8e7;
  }
  * { box-sizing: border-box; margin: 0; padding: 0; }
  html, body {
    width: 1200px; height: 896px; overflow: hidden;
    background: var(--stage);
    font-family: "Lato", sans-serif;
  }
  .stage {
    width: 1200px; height: 896px;
    display: flex; align-items: center; justify-content: center; gap: 60px;
  }
  .card {
    position: relative;
    width: 520px; height: 298px;
    border-radius: 18px;
    background: var(--teal);
    overflow: hidden;
    box-shadow: 0 10px 30px rgba(0,0,0,.18);
    color: var(--white);
  }
  /* Front */
  .card--front {
    display: flex; flex-direction: column; align-items: center; justify-content: center; gap: 22px;
  }
  .brand { display: flex; align-items: center; gap: 16px; }
  .brand__dot { width: 46px; height: 46px; border-radius: 50%; background: var(--white); opacity: .9; flex: none; }
  .brand__name {
    font-weight: 300; font-size: 34px; letter-spacing: 1px; line-height: 1.05;
    color: var(--white);
  }
  .card__handle {
    font-weight: 400; font-size: 14px; letter-spacing: 2px; color: var(--white);
  }
  .brand--small { gap: 9px; }
  .brand--small .brand__dot { width: 22px; height: 22px; }
  .brand--small .brand__name { font-size: 17px; }

  /* Back */
  .card__shapes { position: absolute; inset: 0; }
  .card--back .brand { position: absolute; left: 28px; top: 70px; }
  .nameplate {
    position: absolute; left: 0; top: 150px; width: 340px; height: 62px;
    padding: 10px 28px;
  }
  .nameplate__name { font-weight: 900; font-size: 25px; letter-spacing: .5px; text-transform: uppercase; line-height: 1; }
  .nameplate__role { font-weight: 400; font-size: 14px; margin-top: 5px; }
  .contacts {
    position: absolute; left: 140px; top: 220px;
    list-style: none; font-size: 13px; line-height: 17px;
  }
  .contacts li { display: flex; align-items: center; gap: 8px; }
  .contacts svg { width: 11px; height: 11px; fill: var(--white); flex: none; }
</style>
</head>
<body>
<main class="stage">

  <section class="card card--front" aria-label="Card front">
    <div class="brand">
      <span class="brand__dot"></span>
      <span class="brand__name">Luma Harbor<br>Vow Studio</span>
    </div>
    <p class="card__handle">@sayidoatluma</p>
  </section>

  <section class="card card--back" aria-label="Card back">
    <svg class="card__shapes" viewBox="0 0 520 298" width="520" height="298">
      <defs>
        <radialGradient id="portraitTone" cx="55%" cy="45%" r="60%">
          <stop offset="0" stop-color="#f1c99a"/>
          <stop offset=".6" stop-color="#d9a56e"/>
          <stop offset="1" stop-color="#e9b57c"/>
        </radialGradient>
      </defs>
      <rect x="0" y="150" width="340" height="62" fill="var(--gold)"/>
      <circle cx="462" cy="38" r="168" fill="var(--gold)"/>
      <circle cx="462" cy="38" r="160" fill="url(#portraitTone)" role="img" aria-label="Portrait photo of the owner"/>
    </svg>

    <div class="brand brand--small">
      <span class="brand__dot"></span>
      <span class="brand__name">Luma Harbor<br>Vow Studio</span>
    </div>

    <div class="nameplate">
      <p class="nameplate__name">Delia Brennan</p>
      <p class="nameplate__role">Owner &amp; Officiant</p>
    </div>

    <ul class="contacts">
      <li><svg viewBox="0 0 12 12"><path d="M6 .8a3.6 3.6 0 0 0-3.6 3.6C2.4 7.2 6 11.2 6 11.2s3.6-4 3.6-6.8A3.6 3.6 0 0 0 6 .8zm0 5a1.4 1.4 0 1 1 0-2.8 1.4 1.4 0 0 1 0 2.8z"/></svg>Isabela, Puerto Rico</li>
      <li><svg viewBox="0 0 12 12"><path d="M2.5 1h2l1 2.5-1.3 1a6 6 0 0 0 3.3 3.3l1-1.3L11 7.5v2A1.5 1.5 0 0 1 9.5 11 8.5 8.5 0 0 1 1 2.5 1.5 1.5 0 0 1 2.5 1z"/></svg>555.014.2871</li>
      <li><svg viewBox="0 0 12 12"><path d="M1 2.5h10v7H1zM1.8 3.3 6 6.5l4.2-3.2v.9L6 7.4 1.8 4.2z" fill-rule="evenodd"/></svg>delia@lumaharborvowstudio.com</li>
      <li><svg viewBox="0 0 12 12"><circle cx="6" cy="6" r="5"/></svg>www.lumaharborvowstudio.com</li>
    </ul>
  </section>

</main>
</body>
</html>
```